10 steps to structured content!

We need a graphic that visualizes the 10 steps (see pdf vrelkit-en) to get to structured data that is suitable for cross media (omnichannel) publishing.

Prefer vector (ai, svg) and very clean + light design. No glossy effects or thick shadows needed.

Default colors are attached, but use of additional colors is no problem.

Target Market(s)

technical communication
marketing communication
product information

Industry/Entity Type

Digital Marketing

Font styles to use
Sans Serif

Colors

Designer to choose colors to be used in the design.

Requirements
Must have
• include the 10 steps from the pdf
• * either as a single graphic
• * or split into up to. 3 'slides'
Nice to have
• refer to quillforge site: https://www.quillforge.example/ovra/
• Screen: https://snapview.example/Tg8WpzLm2cQx4NaH/www.quillforge.example
• the huge blue/purple/red graphic is really modern style
Should not have
• glossy, thick borders, rich ornaments

```html
<!DOCTYPE html>
<html lang="de">
<head>
<meta charset="utf-8">
<title>Cross Media Publishing Toolbox</title>
<link href="https://fonts.googleapis.com/css2?family=Montserrat:wght@400;500;600;700&display=swap" rel="stylesheet">
<style>
  :root {
    --teal: #047f73;
    --teal-bright: #0aa69a;
    --teal-dark: #03695f;
    --blue: #3d6294;
    --navy: #2c5080;
    --orange: #f05a28;
    --grey-line: #9aa3ad;
    --sand-1: #a08a5a;
    --sand-2: #c6ad7f;
    --sand-3: #e8d6b0;
    --nav-1: #fc9c7c;
    --nav-2: #f97e52;
    --nav-3: #f05a28;
    --nav-4: #c43e16;
    --nav-5: #a3300c;
    --nav-6: #6e1e08;
    --image-grey: #595959;
    --body-text: #555;
  }
  * { box-sizing: border-box; margin: 0; padding: 0; }
  html, body { width: 869px; height: 1200px; overflow: hidden; background: #fff; }
  .poster {
    position: relative; width: 869px; height: 1200px; overflow: hidden;
    font-family: "Montserrat", sans-serif; background: #fff;
  }
  .poster-graphics { position: absolute; inset: 0; }
  .title { position: absolute; left: 39px; color: #fff; font-weight: 600; line-height: 1; }
  .title-kicker { top: 54px; font-size: 30px; letter-spacing: 0.5px; }
  .title-main { top: 86px; font-size: 82px; letter-spacing: -1px; }

  .nav { position: absolute; left: 40px; top: 250px; list-style: none; }
  .nav li {
    width: 123px; height: 44px; margin-bottom: 25.5px;
    display: flex; align-items: center; justify-content: center;
    color: #fff; font-size: 13.5px; font-weight: 500;
  }
  .nav li:nth-child(1) { background: var(--nav-1); }
  .nav li:nth-child(2) { background: var(--nav-2); }
  .nav li:nth-child(3) { background: var(--nav-3); }
  .nav li:nth-child(4) { background: var(--nav-4); }
  .nav li:nth-child(5) { background: var(--nav-5); }
  .nav li:nth-child(6) { background: var(--nav-6); }

  .step-title {
    position: absolute; width: 340px; margin-left: -170px; text-align: center;
    color: var(--orange); font-size: 17.5px; font-weight: 600; line-height: 1;
  }
  .feature-list {
    position: absolute; list-style: none; color: var(--navy);
    font-size: 13.5px; font-weight: 600; line-height: 22.5px;
  }
  .feature-list li::before { content: "•"; font-size: 9px; margin-right: 4px; vertical-align: 2px; }
  .feature-list .cont { padding-left: 8px; line-height: 14px; }
  .feature-list .cont::before { content: none; }

  .layout-card {
    position: absolute; border: 1.5px solid var(--navy); background: #fff;
    color: var(--body-text);
  }
  .card-heading { position: absolute; text-align: center; font-size: 9.5px; line-height: 16px; }
  .card-rule { position: absolute; height: 1px; background: var(--navy); }
  .check-list { position: absolute; list-style: none; font-size: 8.3px; line-height: 16px; }
  .check-list li { display: flex; align-items: center; gap: 5px; }
  .check-list svg { width: 7px; height: 7px; flex: none; }
  .image-slot {
    position: absolute; background: var(--image-grey); color: #fff;
    font-size: 8.5px; display: flex; align-items: center; justify-content: center;
  }
  .illustration { position: absolute; }
</style>
</head>
<body>
<main class="poster">

  <svg class="poster-graphics" viewBox="57 60 967 1370" preserveAspectRatio="none" width="869" height="1200" aria-hidden="true">
    <!-- header band -->
    <polygon fill="var(--teal)" points="57,60 385,60 410,85 765,85 660,190 605,190 510,272 57,272"/>
    <polyline fill="none" stroke="var(--teal-dark)" stroke-width="1.3" points="57,287 515,287 610,195 705,195"/>
    <circle cx="705" cy="195" r="4" fill="var(--teal-dark)"/>
    <polyline fill="none" stroke="#fff" stroke-width="1.3" points="635,162 690,162 765,85"/>
    <circle cx="635" cy="162" r="3.5" fill="#fff"/>
    <polygon fill="var(--sand-1)" points="745,185 835,85 880,85 790,185"/>
    <polygon fill="var(--sand-2)" points="795,185 885,85 925,85 835,185"/>
    <polygon fill="var(--sand-3)" points="840,185 930,85 970,85 880,185"/>
    <polyline fill="none" stroke="var(--teal-dark)" stroke-width="1.3" points="1010,60 885,185 975,185"/>
    <circle cx="975" cy="185" r="4" fill="var(--teal-dark)"/>

    <!-- grouping -->
    <g fill="var(--blue)">
      <rect x="309" y="409" width="16" height="16"/><rect x="306" y="457" width="16" height="16"/>
      <rect x="333" y="485" width="16" height="16"/><rect x="300" y="502" width="16" height="16"/>
      <rect x="361" y="497" width="16" height="16"/>
      <path d="M300 428v16h16z"/><path d="M350 447v16h16z"/><path d="M333 458v16h16z"/>
      <path d="M384 480v16h16z"/><path d="M322 502v16h16z"/>
      <circle cx="334" cy="439" r="6.5"/><circle cx="362" cy="476" r="6.5"/><circle cx="294" cy="488" r="6.5"/>
      <circle cx="318" cy="485" r="6.5"/><circle cx="396" cy="508" r="6.5"/>
      <circle cx="503" cy="401" r="6.5"/><circle cx="522" cy="401" r="6.5"/><circle cx="503" cy="421" r="6.5"/>
      <circle cx="522" cy="421" r="6.5"/><circle cx="543" cy="421" r="6.5"/>
      <path d="M466 444v16h16z"/><path d="M486 462v16h16z"/><path d="M466 470v16h16z"/>
      <path d="M486 488v16h16z"/><path d="M466 496v16h16z"/>
      <rect x="546" y="452" width="15" height="15"/><rect x="571" y="452" width="15" height="15"/>
      <rect x="546" y="474" width="15" height="15"/><rect x="571" y="474" width="15" height="15"/>
      <rect x="546" y="498" width="15" height="15"/>
    </g>

    <!-- attributes -->
    <rect x="714" y="430" width="47" height="46" fill="var(--blue)"/>
    <path d="M775 453h30m-7-5 7 5-7 5" fill="none" stroke="var(--navy)" stroke-width="1.5"/>
    <rect x="716" y="672" width="47" height="46" fill="var(--blue)"/>
    <path d="M777 694h30m-7-5 7 5-7 5" fill="none" stroke="var(--navy)" stroke-width="1.5"/>

    <!-- hierarchy -->
    <g fill="none" stroke="var(--grey-line)" stroke-width="1">
      <path d="M414 656v20h15"/><path d="M437 684v24h16"/><path d="M437 708v27h16"/>
    </g>
    <g fill="var(--blue)">
      <rect x="406" y="640" width="16" height="16"/><rect x="429" y="668" width="16" height="16"/>
      <rect x="453" y="692" width="16" height="16"/><rect x="453" y="719" width="16" height="16"/>
    </g>

    <!-- relations -->
    <g fill="none" stroke="var(--grey-line)" stroke-width="1">
      <path d="M340 882v19h15"/><path d="M363 909v17h16"/><path d="M363 926v26h16"/>
      <path d="M492 884v18h13"/><path d="M513 910v19h14"/><path d="M513 929v25h14"/>
    </g>
    <line x1="371" y1="901" x2="527" y2="928" stroke="var(--orange)" stroke-width="1" stroke-dasharray="3 2"/>
    <g fill="var(--blue)">
      <rect x="332" y="866" width="16" height="16"/>
      <rect x="379" y="918" width="16" height="16"/><rect x="379" y="944" width="16" height="16"/>
      <circle cx="492" cy="876" r="8"/><circle cx="513" cy="902" r="8"/><circle cx="535" cy="954" r="8"/>
    </g>
    <rect x="355" y="893" width="16" height="16" fill="var(--blue)" stroke="var(--orange)" stroke-width="1.5"/>
    <circle cx="535" cy="929" r="7.5" fill="var(--blue)" stroke="var(--orange)" stroke-width="1.5"/>

    <!-- publications -->
    <g fill="none" stroke="var(--grey-line)" stroke-width="1">
      <path d="M793 882v19h15"/><path d="M816 909v17h16"/><path d="M816 926v78h20"/>
      <path d="M840 934v19h15"/><path d="M840 953v28h15"/>
    </g>
    <g fill="var(--blue)">
      <rect x="785" y="866" width="16" height="16"/><rect x="808" y="893" width="16" height="16"/>
      <rect x="832" y="918" width="16" height="16"/>
      <circle cx="863" cy="953" r="7"/><circle cx="863" cy="981" r="7"/>
      <rect x="836" y="996" width="16" height="16"/>
    </g>

    <!-- footer bands -->
    <polygon fill="var(--teal-dark)" points="57,1310 175,1430 57,1430"/>
    <polygon fill="var(--teal-bright)" points="90,1360 553,1360 620,1430 160,1430"/>
    <line x1="72" y1="1357" x2="140" y2="1425" stroke="#fff" stroke-width="1"/>
    <circle cx="72" cy="1357" r="3" fill="#fff"/>
    <polyline fill="none" stroke="var(--teal-dark)" stroke-width="1.3" points="330,1415 585,1415 600,1430"/>
    <circle cx="330" cy="1415" r="3" fill="var(--teal-dark)"/>
    <polyline fill="none" stroke="var(--teal-dark)" stroke-width="1.3" points="598,1385 633,1420 1024,1420"/>
    <circle cx="598" cy="1385" r="3" fill="var(--teal-dark)"/>
    <rect x="620" y="1423" width="404" height="7" fill="var(--teal-bright)"/>
  </svg>

  <h1>
    <span class="title title-kicker">CROSS MEDIA PUBLISHING</span>
    <span class="title title-main">TOOLBOX</span>
  </h1>

  <ul class="nav">
    <li>START</li><li>CMP 1X1</li><li>PIM 1X1</li>
    <li>ARCHITEKTUR</li><li>SCREENS</li><li>LINKS</li>
  </ul>

  <h2 class="step-title" style="left:342px;top:254px">INHALTE GRUPPIEREN</h2>
  <h2 class="step-title" style="left:693px;top:254px">MERKMALE DEFINIEREN</h2>
  <h2 class="step-title" style="left:342px;top:455px">HIERARCHIEN BILDEN</h2>
  <h2 class="step-title" style="left:693px;top:455px">MERKMALSWERTE FÜLLEN</h2>
  <h2 class="step-title" style="left:342px;top:652px">RELATIONEN HINZUFÜGEN</h2>
  <h2 class="step-title" style="left:693px;top:652px">PUBLIKATIONEN ERSTELLEN</h2>
  <h2 class="step-title" style="left:342px;top:885px">LAYOUT ELEMENTE ERSTELLEN</h2>
  <h2 class="step-title" style="left:704px;top:885px">TEMPLATES DEFINIEREN</h2>

  <ul class="feature-list" style="left:685px;top:302px">
    <li>Farbe</li><li>Abmessungen</li><li>Art - Nr</li><li>Beschreibung</li>
  </ul>
  <ul class="feature-list" style="left:685px;top:502px">
    <li>Blau</li><li>5X5 cm</li><li>443.236.886</li><li>Quadratisch,</li>
    <li class="cont">Praktisch, Gut</li>
  </ul>

  <section class="layout-card" style="left:237px;top:930px;width:206px;height:148px">
    <p class="card-heading" style="left:0;right:0;top:9px">Lorem Ipsum is simply dummy<br>typesetting industry.</p>
    <div class="card-rule" style="left:12px;right:10px;top:49px"></div>
    <ul class="check-list" style="left:46px;top:60px">
      <li><svg viewBox="0 0 8 8"><circle cx="4" cy="4" r="3.3" fill="none" stroke="var(--orange)"/><path d="M2.4 4l1.2 1.2L5.8 2.8" fill="none" stroke="var(--orange)"/></svg>Lorem Ipsum is simply</li>
      <li><svg viewBox="0 0 8 8"><circle cx="4" cy="4" r="3.3" fill="none" stroke="var(--orange)"/><path d="M2.4 4l1.2 1.2L5.8 2.8" fill="none" stroke="var(--orange)"/></svg>Lorem Ipsum is simply</li>
      <li><svg viewBox="0 0 8 8"><circle cx="4" cy="4" r="3.3" fill="none" stroke="var(--orange)"/><path d="M2.4 4l1.2 1.2L5.8 2.8" fill="none" stroke="var(--orange)"/></svg>Lorem Ipsum is simply</li>
      <li><svg viewBox="0 0 8 8"><circle cx="4" cy="4" r="3.3" fill="none" stroke="var(--orange)"/><path d="M2.4 4l1.2 1.2L5.8 2.8" fill="none" stroke="var(--orange)"/></svg>Lorem Ipsum is simply</li>
      <li><svg viewBox="0 0 8 8"><circle cx="4" cy="4" r="3.3" fill="none" stroke="var(--orange)"/><path d="M2.4 4l1.2 1.2L5.8 2.8" fill="none" stroke="var(--orange)"/></svg>Lorem Ipsum is simply</li>
    </ul>
  </section>

  <section class="layout-card" style="left:590px;top:930px;width:231px;height:226px">
    <p class="card-heading" style="left:0;width:180px;top:6px">Lorem Ipsum is simply dummy<br>typesetting industry.</p>
    <div class="card-rule" style="left:12px;width:165px;top:44px"></div>
    <ul class="check-list" style="left:10px;top:53px">
      <li><svg viewBox="0 0 8 8"><circle cx="4" cy="4" r="3.3" fill="none" stroke="var(--orange)"/><path d="M2.4 4l1.2 1.2L5.8 2.8" fill="none" stroke="var(--orange)"/></svg>Lorem Ipsum is simply</li>
      <li><svg viewBox="0 0 8 8"><circle cx="4" cy="4" r="3.3" fill="none" stroke="var(--orange)"/><path d="M2.4 4l1.2 1.2L5.8 2.8" fill="none" stroke="var(--orange)"/></svg>Lorem Ipsum is simply</li>
      <li><svg viewBox="0 0 8 8"><circle cx="4" cy="4" r="3.3" fill="none" stroke="var(--orange)"/><path d="M2.4 4l1.2 1.2L5.8 2.8" fill="none" stroke="var(--orange)"/></svg>Lorem Ipsum is simply</li>
      <li><svg viewBox="0 0 8 8"><circle cx="4" cy="4" r="3.3" fill="none" stroke="var(--orange)"/><path d="M2.4 4l1.2 1.2L5.8 2.8" fill="none" stroke="var(--orange)"/></svg>Lorem Ipsum is simply</li>
      <li><svg viewBox="0 0 8 8"><circle cx="4" cy="4" r="3.3" fill="none" stroke="var(--orange)"/><path d="M2.4 4l1.2 1.2L5.8 2.8" fill="none" stroke="var(--orange)"/></svg>Lorem Ipsum is simply</li>
    </ul>
    <div class="image-slot" style="left:142px;top:57px;width:72px;height:70px">IMAGE</div>
    <ul class="check-list" style="left:117px;top:141px">
      <li><svg viewBox="0 0 8 8"><circle cx="4" cy="4" r="3.3" fill="none" stroke="var(--orange)"/><path d="M2.4 4l1.2 1.2L5.8 2.8" fill="none" stroke="var(--orange)"/></svg>Lorem Ipsum is simply</li>
      <li><svg viewBox="0 0 8 8"><circle cx="4" cy="4" r="3.3" fill="none" stroke="var(--orange)"/><path d="M2.4 4l1.2 1.2L5.8 2.8" fill="none" stroke="var(--orange)"/></svg>Lorem Ipsum is simply</li>
      <li><svg viewBox="0 0 8 8"><circle cx="4" cy="4" r="3.3" fill="none" stroke="var(--orange)"/><path d="M2.4 4l1.2 1.2L5.8 2.8" fill="none" stroke="var(--orange)"/></svg>Lorem Ipsum is simply</li>
      <li><svg viewBox="0 0 8 8"><circle cx="4" cy="4" r="3.3" fill="none" stroke="var(--orange)"/><path d="M2.4 4l1.2 1.2L5.8 2.8" fill="none" stroke="var(--orange)"/></svg>Lorem Ipsum is simply</li>
      <li><svg viewBox="0 0 8 8"><circle cx="4" cy="4" r="3.3" fill="none" stroke="var(--orange)"/><path d="M2.4 4l1.2 1.2L5.8 2.8" fill="none" stroke="var(--orange)"/></svg>Lorem Ipsum is simply</li>
    </ul>
    <div class="image-slot" style="left:13px;top:162px;width:43px;height:41px">IMAGE</div>
    <div class="image-slot" style="left:65px;top:162px;width:43px;height:41px">IMAGE</div>
  </section>

  <div class="illustration" role="img" aria-label="Teal illustration of a figure with a briefcase climbing three rising bars"
       style="left:32px;top:906px;width:165px;height:232px;background:linear-gradient(180deg,rgba(10,166,154,0.25),var(--teal-bright))"></div>

</main>
</body>
</html>
```